Letterhead design for business

Looking for an attractive and professional letterhead that uses the logo that is attached below.

Target Market(s)

Potential bankruptcy clients.

Industry/Entity Type

Legal

Colors

Designer to choose colors to be used in the design.

Requirements
Must have
• Address for locations, phone number, and website address.
• Addresses are on website ferncoveadvice.example. Use following phone number (for tracking purposes): 555-013-8274

```html
<!DOCTYPE html>
<html lang="en">
<head>
<meta charset="utf-8">
<title>Fern Cove Law Group – Letterhead</title>
<link rel="stylesheet" href="https://fonts.googleapis.com/css2?family=Roboto:wght@400;500&display=swap">
<style>
  :root {
    --backdrop: #e9e9e7;
    --paper: #ffffff;
    --green: #6dbb7a;
    --charcoal: #3a3a3b;
    --text: #6b6b6b;
    --text-dark: #3f3f3f;
  }
  * { box-sizing: border-box; margin: 0; padding: 0; }
  html, body {
    width: 1200px; height: 946px; overflow: hidden;
    background: var(--backdrop);
    font-family: "Roboto", Arial, sans-serif;
  }
  .letterhead {
    position: absolute; left: 273px; top: 13px;
    width: 654px; height: 920px;
    background: var(--paper);
    box-shadow: 0 4px 14px rgba(0,0,0,0.18);
    overflow: hidden;
    color: var(--text);
  }
  .brand { position: absolute; left: 50px; top: 64px; display: flex; align-items: center; gap: 12px; }
  .brand-dot { width: 30px; height: 30px; border-radius: 50%; background: var(--green); }
  .brand-text { display: flex; flex-direction: column; }
  .brand-name { font-size: 23px; font-weight: 500; color: var(--green); line-height: 1.05; }
  .brand-attorney { font-size: 9px; color: var(--green); margin-top: 4px; }
  .contact {
    position: absolute; left: 474px; top: 64px;
    font-size: 10.5px; line-height: 15.5px; color: var(--text-dark);
  }
  .contact .gap { height: 4px; }
  .contact-line { display: flex; align-items: center; gap: 5px; }
  .contact-line svg { width: 9px; height: 9px; fill: var(--green); }
  .recipient { position: absolute; left: 55px; top: 268px; font-size: 11.5px; line-height: 17px; }
  .body-copy { position: absolute; left: 55px; width: 543px; font-size: 11.2px; line-height: 17px; text-align: justify; }
  .body-copy.first { top: 372px; }
  .body-copy.second { top: 526px; }
  .signature { position: absolute; left: 54px; top: 617px; width: 125px; height: 82px; background: linear-gradient(120deg, rgba(109,187,122,0.18), rgba(109,187,122,0.05)); }
  .sign-title { position: absolute; left: 54px; top: 715px; font-size: 11.5px; }
  .footer-wave { position: absolute; left: 0; bottom: 0; width: 654px; height: 100px; }
  .footer-url { position: absolute; right: 64px; bottom: 29px; font-size: 10.5px; color: #ffffff; }
</style>
</head>
<body>
  <main class="letterhead">
    <header>
      <div class="brand">
        <div class="brand-dot"></div>
        <div class="brand-text">
          <span class="brand-name">Fern Cove Law Group</span>
          <span class="brand-attorney">by Attorney R. Maldon</span>
        </div>
      </div>
      <address class="contact" style="font-style:normal">
        <div>Level 2, 17 Harbour Lane</div>
        <div>Easton, VIC 3999</div>
        <div class="gap"></div>
        <div class="contact-line">
          <svg viewBox="0 0 10 10"><path d="M2 0.5 L3.6 2.6 L2.8 3.8 Q4 6 6.2 7.2 L7.4 6.4 L9.5 8 L8.4 9.5 Q4.5 9.4 0.5 1.6 Z"/></svg>
          <span>555-013-8274</span>
        </div>
        <div class="contact-line">
          <svg viewBox="0 0 10 10"><path d="M0.5 2 H9.5 V8.5 H0.5 Z M0.5 2 L5 5.6 L9.5 2" stroke="#fff" stroke-width="0.8"/></svg>
          <span>info@ferncoveadvice.example</span>
        </div>
      </address>
    </header>

    <div class="recipient">
      Dear Halvorsen<br>
      Northway Print Company<br>
      Department Design
    </div>

    <p class="body-copy first">Lorem ipsum dolor sit amet, consectetuer adipiscing elit. Aenean commodo ligula eget dolor. Aenean massa. Cum sociis natoque penatibus et magnis dis parturient montes, nascetur ridiculus mus. Donec quam felis, ultricies nec, pellentesque eu, pretium quis, sem. Nulla consequat massa quis enim. Donec pede justo, fringilla vel, aliquet nec, vulputate eget, arcu. In enim justo, rhoncus ut, imperdiet a, venenatis vitae, justo. Nullam dictum felis eu pede mollis pretium. Integer tincidunt. Cras dapibus. Vivamus elementum semper nisi.Nullam dictum felis eu pede mollis pretium. Integer tincidunt. Cras dapibus. Vivamus elementum semper nisi.felis eu pede mollis pretium. Integer tincidunt. Cras dapibus.</p>

    <p class="body-copy second">Quisque rutrum. Aenean imperdiet. Etiam ultricies nisi vel augue. Curabitur ullamcorper ultricies nisi. Nam eget dui. Etiam rhoncus. Maecenas tempus, tellus eget condimentum rhoncus, sem quam semper libero, sit amet adipiscing sem neque sed ipsum.felis pede mollis pretium. I am tincidunt. Cras dapibus.</p>

    <div class="signature" role="img" aria-label="Handwritten signature in green ink"></div>
    <div class="sign-title">Director/Excecutive Director</div>

    <footer>
      <svg class="footer-wave" viewBox="0 0 654 100" preserveAspectRatio="none">
        <path fill="var(--charcoal)" d="M0 28 C60 62 120 70 220 62 C360 50 480 14 654 30 V100 H0 Z"/>
        <path fill="var(--green)" d="M0 20 C60 54 130 62 230 52 C370 38 500 0 635 3 C500 6 370 46 230 60 C130 70 60 62 0 26 Z"/>
      </svg>
      <span class="footer-url">www.ferncoveadvice.example</span>
    </footer>
  </main>
</body>
</html>
```